Car Dealership Poster

Need a poster created to promote our Referrral Program - portrait layout 3'x5'. Below is our Referral Progam website page for referance. See attchaed file for out logo.

https://brantleyautohausnj.example/get-paid-for-referrals/

Colors
00AB8E
00BBA5
67D7C9
C6EFE9
E9F9F6

```html
<!DOCTYPE html>
<html lang="en">
<head>
<meta charset="utf-8">
<title>Brantley Autohaus – Get Paid for Referrals</title>
<link href="https://fonts.googleapis.com/css2?family=Montserrat:ital,wght@0,800;0,900;1,900&family=Poppins:wght@400;500;600;700;800&display=swap" rel="stylesheet">
<style>
  :root {
    --green-deep: #1f6239;
    --green-mid: #2c8a55;
    --green-glow: #43a56c;
    --green-chip: #3f9d63;
    --navy: #1d2331;
    --ink: #14161c;
    --white: #ffffff;
    --silver: #d6d6d6;
    --stage: #e5e5e5;
    --text: #2a2a2a;
  }
  * { box-sizing: border-box; margin: 0; padding: 0; }
  html, body { width: 849px; height: 1200px; overflow: hidden; }
  body { background: var(--stage); font-family: "Poppins", sans-serif; position: relative; }

  .poster {
    position: absolute; left: 76px; top: 20px;
    width: 697px; height: 1160px;
    background: var(--white); overflow: hidden;
  }
  .poster__backdrop { position: absolute; inset: 0; width: 697px; height: 780px; }

  .headline {
    position: absolute; white-space: nowrap;
    font-family: "Montserrat", sans-serif; font-weight: 900; font-style: italic;
    line-height: 1;
    background: linear-gradient(180deg, var(--white) 30%, var(--silver) 100%);
    -webkit-background-clip: text; background-clip: text; color: transparent;
    filter: drop-shadow(0 3px 3px rgba(0,0,0,.3));
  }
  .headline--top { top: 42px; left: 46px; font-size: 86px; letter-spacing: -3px; }
  .headline--bottom { top: 122px; left: 84px; font-size: 90px; letter-spacing: -1px; }

  .tag-for {
    position: absolute; left: 486px; top: 50px; width: 160px; height: 64px;
    background: var(--green-chip); border-radius: 10px;
    box-shadow: 0 4px 8px rgba(0,0,0,.3);
    display: flex; align-items: center; justify-content: center;
    font-family: "Montserrat", sans-serif; font-weight: 900; font-style: italic;
    font-size: 52px; letter-spacing: -1px; color: #eeeeee;
  }

  .reward-icon {
    position: absolute; left: 33px; top: 254px; width: 138px; height: 152px;
    border-radius: 16px;
    background: linear-gradient(160deg, #f3f3f3 0%, #f6c6b3 55%, #1d2331 100%);
    opacity: .85;
  }

  .reward {
    position: absolute; left: 193px; top: 254px; white-space: nowrap;
    font-family: "Montserrat", sans-serif; font-weight: 900; font-style: italic;
    font-size: 82px; letter-spacing: -2.5px; line-height: 1;
    background: linear-gradient(180deg, var(--white) 30%, var(--silver) 100%);
    -webkit-background-clip: text; background-clip: text; color: transparent;
    filter: drop-shadow(0 3px 3px rgba(0,0,0,.3));
  }
  .reward-sub {
    position: absolute; left: 186px; top: 325px; white-space: nowrap;
    font-family: "Montserrat", sans-serif; font-weight: 900; font-style: italic;
    font-size: 62px; letter-spacing: -1.5px; line-height: 1; color: var(--navy);
    text-shadow: 0 3px 4px rgba(0,0,0,.25);
  }

  .photo-car {
    position: absolute; left: 0; top: 418px; width: 475px; height: 312px;
    background: linear-gradient(160deg, #3a3d42 0%, #141518 55%, #0a0a0c 100%);
    border-radius: 140px 90px 40px 60px / 70px 60px 40px 50px;
  }
  .photo-person {
    position: absolute; left: 408px; top: 387px; width: 289px; height: 393px;
    background: linear-gradient(180deg, #d9b27a 0%, #e7c093 30%, #f0b43a 62%, #f6c65a 100%);
    border-radius: 140px 140px 0 0;
  }

  .promise {
    position: absolute; left: 23px; top: 783px; width: 656px; height: 131px;
    background: linear-gradient(100deg, var(--ink) 0%, #222735 100%);
    border: 3px solid #ececec; border-radius: 22px;
    box-shadow: 0 4px 8px rgba(0,0,0,.25);
    display: flex; align-items: center; justify-content: center; padding: 0 10px;
    color: var(--white); font-weight: 700; font-size: 24.5px; line-height: 1.32;
    text-align: center; letter-spacing: -.9px; white-space: nowrap;
  }

  .terms { position: absolute; left: 44px; top: 938px; width: 622px; }
  .terms__item {
    position: relative; padding-left: 20px;
    font-size: 15.4px; line-height: 1.5; color: var(--text); text-align: justify;
    letter-spacing: .15px;
  }
  .terms__item::before {
    content: ""; position: absolute; left: 1px; top: 8px;
    width: 10px; height: 10px; border-radius: 50%; background: var(--green-deep);
  }
  .terms__note { margin-top: 12px; font-size: 16.2px; font-weight: 500; color: #111; white-space: nowrap; letter-spacing: -.1px; }
  .terms__note em { font-style: normal; color: var(--green-deep); }

  .contact { position: absolute; left: 34px; top: 1046px; font-style: normal; }
  .contact__row { display: flex; align-items: center; gap: 13px; }
  .contact__row + .contact__row { margin-top: 8px; align-items: flex-start; }
  .contact__icon { width: 29px; height: 29px; flex: none; }
  .contact__phone { font-size: 27px; font-weight: 800; color: #111; letter-spacing: .3px; }
  .contact__phone span { color: var(--green-deep); }
  .contact__address { font-size: 12.4px; font-weight: 500; color: #222; line-height: 1.55; }

  .brand {
    position: absolute; left: 366px; top: 1044px; width: 300px;
    display: flex; align-items: center; gap: 10px;
    color: var(--green-deep); font-weight: 800; line-height: 1;
  }
  .brand__dot { width: 22px; height: 22px; border-radius: 50%; background: var(--green-deep); flex: none; }
  .brand__name { font-size: 42px; letter-spacing: -1px; }
  .brand__name small { display: block; font-size: 27px; letter-spacing: 7px; margin-top: 4px; }
</style>
</head>
<body>
  <main class="poster">
    <svg class="poster__backdrop" viewBox="0 0 697 780" aria-hidden="true">
      <defs>
        <radialGradient id="bandGlow" cx="0.45" cy="0.35" r="0.7">
          <stop offset="0" stop-color="#45a872"/>
          <stop offset="1" stop-color="#23693f"/>
        </radialGradient>
      </defs>
      <path d="M0 0 H697 V508 C640 540 560 600 470 700 C380 780 150 790 0 718 Z" fill="var(--green-deep)"/>
      <path d="M0 236 L697 218 V440 L0 458 Z" fill="url(#bandGlow)"/>
      <path d="M0 236 L697 218" stroke="#7dbb93" stroke-width="2" opacity=".6"/>
      <path d="M0 458 L697 440" stroke="#7dbb93" stroke-width="2" opacity=".6"/>
    </svg>

    <h1>
      <span class="headline headline--top">GET PAID</span>
      <span class="tag-for">FOR</span>
      <span class="headline headline--bottom">REFERRALS</span>
    </h1>

    <div class="reward-icon" role="img" aria-label="Icon illustration of a handshake beneath a dollar coin"></div>

    <p class="reward">EARN $250</p>
    <p class="reward-sub">PER REFERRAL</p>

    <div class="photo-car" role="img" aria-label="Photo of a black compact sedan, front three-quarter view"></div>
    <div class="photo-person" role="img" aria-label="Photo of a smiling woman in a yellow shirt pointing at the viewer"></div>

    <p class="promise">We love Referrals and you will too! Earn a<br>$250 referral credit everytime a referral of<br>yours buys a vehicle from us.</p>

    <section class="terms">
      <p class="terms__item">Applied as credit and can be used towards the purchase of a vehicle or towards Coastal Line Auto Finance loan payments.</p>
      <p class="terms__note">*Referral must be a new customer to Brantley Autohaus... <em>No cash value.</em></p>
    </section>

    <address class="contact">
      <div class="contact__row">
        <svg class="contact__icon" viewBox="0 0 29 29" aria-hidden="true">
          <circle cx="14.5" cy="14.5" r="14.5" fill="var(--green-deep)"/>
          <path d="M10 7.5 L12.5 7 L14 11 L12.3 12.5 C13 14.5 14.5 16 16.5 16.7 L18 15 L22 16.5 L21.5 19 C21 20.5 19 21.5 17 20.8 C12.5 19.2 9.8 16.5 8.2 12 C7.5 10 8.5 8 10 7.5 Z" fill="var(--white)"/>
        </svg>
        <span class="contact__phone">(609) <span>555-0187</span></span>
      </div>
      <div class="contact__row">
        <svg class="contact__icon" viewBox="0 0 29 29" aria-hidden="true">
          <circle cx="14.5" cy="14.5" r="14.5" fill="var(--green-deep)"/>
          <path d="M14.5 6.5 C11 6.5 8.5 9 8.5 12.3 C8.5 16.5 14.5 22.5 14.5 22.5 C14.5 22.5 20.5 16.5 20.5 12.3 C20.5 9 18 6.5 14.5 6.5 Z" fill="var(--white)"/>
          <circle cx="14.5" cy="12.4" r="2.4" fill="var(--green-deep)"/>
        </svg>
        <span class="contact__address">212 Harbor Ave, Millbrook,<br>NJ 08099</span>
      </div>
    </address>

    <div class="brand">
      <span class="brand__dot" aria-hidden="true"></span>
      <span class="brand__name">BRANTLEY<small>AUTOHAUS</small></span>
    </div>
  </main>
</body>
</html>
```